Brookmere Osteopathy flyer

I want a clean clear DL flyer (but also want an A4 poster) promoting a new Osteopathic business in a semi rural area in Tasmania (Australia).
It can have pictures like the examples attached to show people what Osteopathy is (its like Chiropractic and physiotherapy).
I am the sole practioner and am male, so any pictures would be best to be a white male if possible.
I've attached some wording, you can use all, or none of it
I don't have a phone number for the business yet
info@brookmereosteopathy.example
www.brookmereosteopathy.example
Target Market(s)
Australians, from tradies, professionals, babies to retired people
Industry/Entity Type
Health
Look and feel

```html
<!DOCTYPE html>
<html lang="en">
<head>
<meta charset="utf-8">
<title>Brookmere Osteopathy Flyer</title>
<link href="https://fonts.googleapis.com/css2?family=Montserrat:wght@700&family=Roboto:wght@300;400;700&family=Lato:wght@400;700&display=swap" rel="stylesheet">
<style>
  :root {
    --backdrop: #a8a8a8;
    --brand-blue: #0b97d3;
    --accent-orange: #f5923a;
    --bullet-gold: #e8b052;
    --paper: #ffffff;
    --title-white: #edf1f6;
    --ink: #1d2a3a;
    --photo-light: #dfe3e8;
    --photo-skin: #d9a98c;
    --photo-dark: #2b3440;
  }
  * { margin: 0; padding: 0; box-sizing: border-box; }
  html, body { width: 1200px; height: 2309px; overflow: hidden; background: var(--backdrop); }
  .stage { position: absolute; left: 0; top: 0; width: 1339px; height: 2576px; transform: scale(0.89619); transform-origin: 0 0; }
  .flyer { position: absolute; left: 82px; top: 90px; width: 1178px; height: 2400px; background: var(--brand-blue); box-shadow: 0 4px 14px rgba(0,0,0,.35); overflow: hidden; }
  .flyer-art { position: absolute; left: 0; top: 0; }
  .abs { position: absolute; }
  .brand-title { left: 0; width: 1178px; top: 336px; text-align: center; font: 700 76px/1 'Montserrat', sans-serif; color: var(--title-white); letter-spacing: 0.5px; }
  .reasons-heading { left: 100px; top: 1432px; font: 700 45px/55px 'Roboto', sans-serif; color: var(--paper); }
  .rule { height: 3px; width: 62px; background: var(--accent-orange); }
  .reasons-list { list-style: none; font: 400 31px/38px 'Lato', sans-serif; color: var(--paper); }
  .reasons-list li { position: relative; padding-left: 45px; }
  .reasons-list li::before { content: ""; position: absolute; left: 2px; top: 11px; width: 15px; height: 15px; border-radius: 50%; background: var(--bullet-gold); }
  .col-1 { left: 100px; top: 1630px; }
  .col-2 { left: 485px; top: 1630px; }
  .col-3 { left: 828px; top: 1629px; }
  .about-heading { left: 109px; top: 1932px; font: 700 47px/1 'Roboto', sans-serif; color: var(--paper); }
  .about-heading span { font-weight: 300; }
  .about-text { left: 374px; top: 1885px; width: 720px; font: 400 26.5px/39px 'Lato', sans-serif; color: var(--paper); }
  .footer { position: absolute; left: 0; top: 2113px; width: 1178px; height: 287px; background: var(--paper); }
  .footer-mark { position: absolute; left: 67px; top: 72px; width: 156px; height: 156px; border-radius: 50%; border: 3px solid var(--brand-blue); }
  .footer-name { position: absolute; left: 243px; top: 120px; font: 700 29px/33px 'Roboto', sans-serif; color: var(--ink); }
  .footer-name span { display: block; font-weight: 400; }
  .contact { position: absolute; left: 588px; top: 42px; list-style: none; font: 400 30px/38px 'Roboto', sans-serif; color: var(--ink); }
  .contact li { position: relative; padding-left: 43px; }
  .contact svg { position: absolute; left: 0; top: 8px; width: 26px; height: 26px; }
  .contact b { font-weight: 700; }
</style>
</head>
<body>
<div class="stage">
  <div class="flyer">
    <svg class="flyer-art" width="1178" height="2400" viewBox="0 0 1178 2400">
      <defs>
        <linearGradient id="heroTone" x1="0" y1="0" x2="1" y2="1">
          <stop offset="0" stop-color="var(--photo-light)"/>
          <stop offset="0.45" stop-color="var(--photo-skin)"/>
          <stop offset="1" stop-color="var(--photo-dark)"/>
        </linearGradient>
        <linearGradient id="babyTone" x1="0" y1="0" x2="0" y2="1">
          <stop offset="0" stop-color="#d7c9cf"/><stop offset="1" stop-color="#5ea3cf"/>
        </linearGradient>
        <linearGradient id="shoulderTone" x1="0" y1="0" x2="1" y2="1">
          <stop offset="0" stop-color="#efe9e6"/><stop offset="1" stop-color="#c98e6c"/>
        </linearGradient>
        <linearGradient id="backTone" x1="0" y1="0" x2="1" y2="1">
          <stop offset="0" stop-color="#b9c7cf"/><stop offset="1" stop-color="#d8a37f"/>
        </linearGradient>
      </defs>
      <!-- top mark -->
      <circle cx="588" cy="175" r="130" fill="none" stroke="var(--paper)" stroke-width="3"/>
      <!-- hero photo area -->
      <path role="img" aria-label="Photo: osteopath gently treating a patient's neck and head on a treatment table" d="M0 588 Q589 400 1178 588 L1178 1310 Q589 1100 0 1310 Z" fill="url(#heroTone)"/>
      <path d="M0 585 Q589 400 1178 585" fill="none" stroke="var(--accent-orange)" stroke-width="30"/>
      <!-- treatment circles -->
      <circle role="img" aria-label="Photo: gentle head treatment for a newborn baby" cx="205" cy="1225" r="153" fill="url(#babyTone)" stroke="var(--paper)" stroke-width="10"/>
      <circle role="img" aria-label="Photo: hands working on a patient's shoulder" cx="588" cy="1128" r="153" fill="url(#shoulderTone)" stroke="var(--paper)" stroke-width="10"/>
      <circle role="img" aria-label="Photo: hands treating a patient's upper back" cx="973" cy="1225" r="153" fill="url(#backTone)" stroke="var(--paper)" stroke-width="10"/>
    </svg>

    <h1 class="abs brand-title">Brookmere Osteopathy</h1>

    <h2 class="abs reasons-heading">Common reasons<br>people visit an osteopath</h2>
    <div class="abs rule" style="left:100px; top:1581px;"></div>

    <ul class="abs reasons-list col-1">
      <li style="margin-bottom:14px;">Back / neck pain</li>
      <li style="margin-bottom:20px;">Headaches / migraines</li>
      <li style="margin-bottom:19px;">Joint and muscle pain</li>
      <li>Pregnancy-related<br>discomfort</li>
    </ul>
    <ul class="abs reasons-list col-2">
      <li style="margin-bottom:13px;">Disc related issues</li>
      <li style="margin-bottom:20px;">Sciatica</li>
      <li style="margin-bottom:14px;">Plantar fasciitis</li>
      <li>Tendonitis / Bursitis</li>
    </ul>
    <ul class="abs reasons-list col-3">
      <li style="margin-bottom:24px;">Adhesive capsulitis<br>(frozen shoulder)</li>
      <li>Tennis<br>/ Golfers elbow</li>
    </ul>

    <h2 class="abs about-heading">about <span>us.</span></h2>
    <div class="abs rule" style="left:109px; top:2001px;"></div>
    <p class="abs about-text">Osteopaths use a combination of joint manipulation, targeted deep tissue massage and stretching to improve function, relieve pain and support the body’s ability to heal itself.</p>

    <footer class="footer">
      <div class="footer-mark"></div>
      <p class="footer-name">Brookmere Osteopathy<span>&amp; Dry Needling</span></p>
      <ul class="contact">
        <li>
          <svg viewBox="0 0 24 24"><path d="M12 2a7 7 0 0 0-7 7c0 5 7 13 7 13s7-8 7-13a7 7 0 0 0-7-7z" fill="none" stroke="var(--ink)" stroke-width="2"/><circle cx="12" cy="9" r="2.5" fill="var(--ink)"/></svg>
          48 Ferncliff Lane,<br>Brookmere
        </li>
        <li>
          <svg viewBox="0 0 24 24"><path d="M6.6 10.8a15 15 0 0 0 6.6 6.6l2.2-2.2a1 1 0 0 1 1-.25 11.4 11.4 0 0 0 3.6.57 1 1 0 0 1 1 1V20a1 1 0 0 1-1 1A17 17 0 0 1 3 4a1 1 0 0 1 1-1h3.5a1 1 0 0 1 1 1c0 1.25.2 2.45.57 3.57a1 1 0 0 1-.25 1z" fill="var(--ink)"/></svg>
          <b>Phone:</b> 1.800.555.0199
        </li>
        <li>
          <svg viewBox="0 0 24 24"><circle cx="12" cy="12" r="9" fill="none" stroke="var(--ink)" stroke-width="2"/><path d="M3 12h18M12 3c3 3 3 15 0 18M12 3c-3 3-3 15 0 18M5 7.5h14M5 16.5h14" fill="none" stroke="var(--ink)" stroke-width="1.5"/></svg>
          www.brookmereosteopathy.example
        </li>
        <li>
          <svg viewBox="0 0 24 24"><rect x="2" y="5" width="20" height="14" fill="var(--ink)"/><path d="M2 5l10 8 10-8" fill="none" stroke="var(--paper)" stroke-width="1.5"/></svg>
          info@brookmereosteopathy.example
        </li>
      </ul>
    </footer>
  </div>
</div>
</body>
</html>
```